Plumbing Business Card Design

our business is a plumbing business.
we would like to see designs with our LOGO featured and then either purple or black writing with a white back ground
or black back ground with white or purple writing or even a purple card!
one option we would love to see is if you could get the TKR letters away from the white background ( it is currently in a white box as a jpeg )it is currently on and overlay it onto black.
FRONT
TKR image to be displayed on the front, please use the attached picture. ( you can remove the email address and mobile number from the botttom and re write it in different font or in a different place on the front.
Directly under the large TKR we would like the words Tidewell Kern Plumbing.
could be spread out like this T I D E W E L L K E R N
P L U M B I N G
We really are open to suggestions though!
Also on the front of the card we could like our little catch phrase somewhere Brindle's Local Plumber

we dont want in plumbing pictures or photos but we are open to swirl across the card or water movement or droplets.

BACK
These services need to be dot pointed or listed on the back
Hot & Cold Water Services
Gas Fitting
Bathroom & Kitchen Renovations
Metal Roofing & Guttering
New Homes & Extensions
Hot Water Service Changeovers
Drainage & Stormwater Works
All General Plumbing & Maitenance

in smaller writing or down the bottom of the card on the back please display write this Lic. No 473918

Contact Information for Business Card

Colm Kern
Mobile: 0427 391 206
email: tidewellkernplumbing@mailnest.example
FInd Us on Facebook Tidewell Kern Plumbing ( with the f symbol ) either on the front or the back

```html
<!DOCTYPE html>
<html lang="en">
<head>
<meta charset="utf-8">
<title>Tidewell Kern Plumbing – Business Card</title>
<link rel="stylesheet" href="https://fonts.googleapis.com/css2?family=Montserrat:wght@400;500;700;800&display=swap">
<style>
  :root {
    --page-bg: #e9e9ec;
    --brand-blue: #2f5ce6;
    --deep-blue: #1c3fb8;
    --violet: #6a4fe0;
    --card-white: #ffffff;
    --ink-grey: #5c5f6b;
    --rule-blue: #8fa6ee;
  }
  * { box-sizing: border-box; margin: 0; padding: 0; }
  html, body {
    width: 1200px; height: 1000px; overflow: hidden;
    background: var(--page-bg);
    font-family: "Montserrat", sans-serif;
  }
  .sheet {
    position: relative; width: 1200px; height: 1000px;
    display: flex; flex-direction: column; align-items: center;
    justify-content: center; gap: 30px;
  }
  .card {
    position: relative; width: 800px; height: 457px;
    overflow: hidden;
    box-shadow: 0 6px 18px rgba(0,0,0,.18);
  }
  .card-shapes { position: absolute; inset: 0; }

  /* Front */
  .card--front { background: var(--card-white); }
  .wordmark {
    position: absolute; left: 100px; top: 120px; width: 260px;
    text-align: center; color: var(--brand-blue); font-weight: 800;
  }
  .wordmark__initials { font-size: 86px; line-height: 1; letter-spacing: 6px; }
  .wordmark__name { font-size: 15px; letter-spacing: 0.5px; margin-top: 4px; }
  .contact {
    position: absolute; left: 395px; top: 170px; width: 345px;
    color: var(--ink-grey);
  }
  .contact__name {
    color: var(--brand-blue); font-weight: 700; font-size: 30px;
    padding-bottom: 10px; border-bottom: 1px dashed var(--rule-blue);
    margin-bottom: 14px; width: 240px;
  }
  .contact__line {
    display: flex; align-items: center; gap: 10px;
    font-size: 14px; margin-bottom: 8px; white-space: nowrap;
  }
  .contact__line svg { flex: none; }
  .contact__rule {
    width: 240px; border-bottom: 1px dashed var(--rule-blue); margin-top: 14px;
  }
  .social {
    position: absolute; left: 60px; bottom: 14px;
    display: flex; align-items: center; gap: 10px;
    color: var(--card-white); font-size: 16px; font-weight: 500;
  }
  .social__dot {
    width: 14px; height: 14px; border-radius: 50%; background: var(--card-white);
  }

  /* Back */
  .card--back { background: var(--brand-blue); }
  .card--back .wordmark {
    left: 0; right: 0; width: auto; top: 60px; color: var(--deep-blue);
  }
  .card--back .wordmark__initials { font-size: 110px; }
  .card--back .wordmark__name { font-size: 20px; }
  .services {
    position: absolute; left: 30px; right: 30px; top: 262px;
    color: var(--card-white); text-align: center;
    font-size: 13.5px; line-height: 1.6; font-weight: 500;
  }
  .services span.sep { padding: 0 6px; }
  .licence-band {
    position: absolute; left: 0; right: 0; bottom: 46px; height: 28px;
    background: var(--card-white); color: var(--brand-blue);
    text-align: center; font-size: 15px; font-weight: 700; line-height: 28px;
  }
  .licence-band::after {
    content: ""; position: absolute; left: 0; right: 0; bottom: -30px;
    height: 6px; background: var(--card-white);
  }
</style>
</head>
<body>
<main class="sheet">

  <section class="card card--front" aria-label="Business card front">
    <svg class="card-shapes" viewBox="0 0 800 457" aria-hidden="true">
      <polygon points="0,0 360,0 400,34 0,50" fill="var(--brand-blue)"/>
      <polygon points="0,56 400,40 404,46 0,62" fill="var(--violet)"/>
      <polygon points="0,407 520,407 560,457 0,457" fill="var(--brand-blue)"/>
      <polygon points="800,310 800,457 590,457" fill="var(--brand-blue)"/>
      <polygon points="800,330 800,362 660,457 632,457" fill="var(--violet)"/>
    </svg>

    <div class="wordmark">
      <div class="wordmark__initials">TKR</div>
      <div class="wordmark__name">TIDEWELL KERN PLUMBING</div>
    </div>

    <div class="contact">
      <div class="contact__name">Colm Kern</div>
      <div class="contact__line">
        <svg width="14" height="16" viewBox="0 0 14 16"><rect x="2" y="1" width="10" height="14" rx="2" fill="none" stroke="var(--brand-blue)" stroke-width="1.6"/><circle cx="7" cy="12.5" r="1" fill="var(--brand-blue)"/></svg>
        <span>0427 391 206</span>
      </div>
      <div class="contact__line">
        <svg width="16" height="12" viewBox="0 0 16 12"><rect x="1" y="1" width="14" height="10" rx="1" fill="none" stroke="var(--brand-blue)" stroke-width="1.6"/><polyline points="1,1 8,7 15,1" fill="none" stroke="var(--brand-blue)" stroke-width="1.6"/></svg>
        <span>tidewellkernplumbing@mailnest.example</span>
      </div>
      <div class="contact__rule"></div>
    </div>

    <div class="social">
      <span class="social__dot"></span>
      <span>fb/tidewellkernplumbing</span>
    </div>
  </section>

  <section class="card card--back" aria-label="Business card back">
    <div class="wordmark">
      <div class="wordmark__initials">TKR</div>
      <div class="wordmark__name">TIDEWELL KERN PLUMBING</div>
    </div>

    <p class="services">
      Hot &amp; Cold Water Services<span class="sep">|</span>Gas Fitting<span class="sep">|</span>Bathroom &amp; Kitchen Renovations<span class="sep">|</span>Metal Roofing &amp; Guttering<br>
      New Homes &amp; Extensions<span class="sep">|</span>Hot Water Service Changeovers<span class="sep">|</span>Drainage &amp; Stormwater Works<br>
      All General Plumbing &amp; Maitenance
    </p>

    <div class="licence-band">Lic. No 473918</div>
  </section>

</main>
</body>
</html>
```